Feldwende Bureau GmbH needs a Letterhead

Need a Letter/Card head based on the logo and Webpage design.
To be used for Business letters and One-Page Handouts with the discription of our different Services.
Cards to be used as Flyers to print on different Topics.
Should be Topic nutral as we do Sabbatical-Consultancy, Coaching, Job-Coaching and Vision-Board Workshops (more to come). See www.feldwendebureau.ch

Target Market(s)

Individuales who need Sabbatical-Support/Coaching/JOB-Coaching
Companies who want to give me a mandate as Business Coach

Industry/Entity Type

Business

Font styles to use
Other font styles liked:
• Verdana

Colors
9ccb3b
3277b5
aaaaaa
eaeaea

Requirements
Must have
• Background White or light gray
• not to big/present the Information on Company-Adresse/phone/email/web/offices
• Use the Logo (chair) in a creative way
• Please use following Colors:
• Green: R141, G198, B63
• Blue: R28, G117, B188
• Darkgray: R109, G110, B113
• Lightgray: R209, G211, B212
Should not have
• Wrong Colors!
• Use mentioned Color codes above.

```html
<!DOCTYPE html>
<html lang="en">
<head>
<meta charset="utf-8">
<title>Feldwende Bureau – Letterhead</title>
<link rel="stylesheet" href="https://fonts.googleapis.com/css2?family=Arimo:wght@400;700&display=swap">
<style>
  :root {
    --green: #8dc63f;
    --blue: #1c75bc;
    --dark-gray: #6d6e71;
    --light-gray: #d1d3d4;
    --paper: #f8f8f8;
    --ink: #161616;
    --white: #ffffff;
  }
  html, body {
    margin: 0;
    padding: 0;
    width: 978px;
    height: 1200px;
    overflow: hidden;
  }
  body {
    font-family: "Arimo", Arial, sans-serif;
    color: var(--ink);
  }
  .letterhead {
    position: relative;
    width: 978px;
    height: 1200px;
    background: linear-gradient(160deg, var(--white) 0%, var(--paper) 55%, #f1f1f1 100%);
    overflow: hidden;
  }
  .brand {
    position: absolute;
    left: 76px;
    top: 74px;
    display: flex;
    align-items: center;
    gap: 16px;
  }
  .brand-dot {
    width: 34px;
    height: 34px;
    border-radius: 50%;
    background: var(--green);
  }
  .brand-name {
    font-size: 40px;
    font-weight: 400;
    color: var(--dark-gray);
    letter-spacing: 0.5px;
  }
  .recipient {
    position: absolute;
    left: 86px;
    top: 256px;
    font-size: 16px;
    line-height: 26px;
  }
  .letter-body {
    position: absolute;
    left: 86px;
    top: 318px;
    width: 800px;
    font-size: 16.5px;
    line-height: 27px;
  }
  .letter-body p {
    margin: 0 0 27px;
  }
  .closing {
    position: absolute;
    left: 86px;
    top: 858px;
    font-size: 16px;
  }
  .signature {
    position: absolute;
    left: 86px;
    top: 884px;
    width: 142px;
    height: 58px;
    border-radius: 4px;
    background: linear-gradient(90deg, #e6e6e6, #f0f0f0);
  }
  .signer {
    position: absolute;
    left: 88px;
    top: 955px;
    font-size: 16.5px;
    font-weight: 700;
  }
  .footer-wave {
    position: absolute;
    left: 0;
    top: 1040px;
    width: 978px;
    height: 160px;
    display: block;
  }
  .contact {
    position: absolute;
    left: 80px;
    top: 1110px;
    margin: 0;
    padding: 0;
    list-style: none;
    color: var(--white);
    font-size: 16px;
    line-height: 23px;
  }
  .contact li {
    display: flex;
    align-items: center;
    gap: 7px;
  }
  .contact svg {
    width: 13px;
    height: 13px;
    flex: none;
  }
</style>
</head>
<body>
<main class="letterhead">
  <header class="brand">
    <span class="brand-dot"></span>
    <span class="brand-name">Feldwende Bureau</span>
  </header>

  <div class="recipient">
    Lorem Ipsum<br>
    Lorem Ipsum Admin
  </div>

  <section class="letter-body">
    <p>Lorem Ipsum is simply dummy text of the printing and typesetting industry. Lorem Ipsum has been the industry's standard dummy text ever since the 1500s, when an unknown printer took a galley of type and scrambled it to make a type specimen book. It has survived not only five centuries, but also the leap into electronic typesetting, remaining essentially unchanged.</p>
    <p>Lorem Ipsum is simply dummy text of the printing and typesetting industry. Lorem Ipsum has been the industry's standard dummy text ever since the 1500s, when an unknown printer took a galley of type and scrambled it to make a type specimen book.</p>
    <p>It has survived not only five centuries, but also the leap into electronic typesetting, remaining essentially unchanged. Lorem Ipsum is simply dummy text of the printing and typesetting industry. Lorem Ipsum has been the industry's standard dummy text ever since the 1500s, when an unknown printer took a galley of type and scrambled</p>
    <p>Lorem Ipsum is simply dummy text of the printing and typesetting industry. Lorem Ipsum has been the industry's standard dummy text ever since the 1500s, when an unknown printer took a galley of type and scrambled it to make a type specimen book. It has survived not only five centuries, but also the leap into electronic typesetting, remaining essentially unchanged.</p>
  </section>

  <div class="closing">Lorem Ipsum</div>
  <div class="signature" role="img" aria-label="Handwritten signature"></div>
  <div class="signer">Lorem Ipsum Admin</div>

  <svg class="footer-wave" viewBox="0 0 978 160" preserveAspectRatio="none" aria-hidden="true">
    <path d="M0 16 C260 6 560 72 978 98 L978 160 L0 160 Z" fill="var(--green)"/>
    <path d="M0 32 C260 22 560 88 978 112 L978 160 L0 160 Z" fill="var(--white)"/>
    <path d="M0 38 C260 30 560 96 978 120 L978 160 L0 160 Z" fill="var(--blue)"/>
    <path d="M520 112 C680 140 820 148 940 146" fill="none" stroke="var(--white)" stroke-width="1.2" opacity="0.8"/>
  </svg>

  <ul class="contact">
    <li>
      <svg viewBox="0 0 14 14"><circle cx="7" cy="7" r="6" fill="none" stroke="#fff" stroke-width="1"/><path d="M4.5 3.8 L6 5.5 L5.2 6.4 Q6.2 8.2 7.7 8.9 L8.6 8.1 L10.2 9.5 L9.2 10.6 Q5.5 9.8 3.5 5 Z" fill="#fff"/></svg>
      +41 (0) 61 555 48 20
    </li>
    <li>
      <svg viewBox="0 0 14 14"><rect x="1.5" y="4" width="11" height="7" fill="none" stroke="#fff" stroke-width="1.3"/><path d="M1.5 4 L7 8 L12.5 4" fill="none" stroke="#fff" stroke-width="1.3"/></svg>
      lena.brunner@feldwendebureau.ch
    </li>
    <li>
      <svg viewBox="0 0 14 14"><path d="M7 13 C3.5 8.5 2.5 7 2.5 5.5 A4.5 4.5 0 0 1 11.5 5.5 C11.5 7 10.5 8.5 7 13 Z" fill="#fff"/><circle cx="7" cy="5.5" r="1.8" fill="var(--blue)"/></svg>
      Lena Brunner, Talackerweg 18, 4153 Reinach, Schweiz
    </li>
  </ul>
</main>
</body>
</html>
```